Modern Irish Pub. We need to find "our look" for new bar.

We have a logo, color scheme and feel of what we want but we need someone to work with to create flyer designs, menu, website and social content.

Young vibrant mixed with traditional Irish. Think neon & sexy mixed with wood and traditional Irish.

Looking for examples of social media posts and flyers. We can then hire for more work! We need to find “our look”.

Target Market(s)

21-40 year olds

Industry/Entity Type

Bar and Restaurant.

Colors
EB3D1F
EC4F4E
F09395
F8D3D4
FCEDEE

Requirements
Must have
• Our logo.
Nice to have
• Young mixed with traditional. Sexy l, vibrant and fun.
Should not have
• Cartoon like child like look and feel.

```html
<!DOCTYPE html>
<html lang="en">
<head>
<meta charset="utf-8">
<title>Brannigan's – Pub Social & Menu Set</title>
<link rel="stylesheet" href="https://fonts.googleapis.com/css2?family=Share+Tech+Mono&family=Oswald:wght@400;500&family=Antonio:wght@400&display=swap">
<style>
  :root{
    --pub-red:#e30b17;
    --neon:#ffd9da;
    --neon-glow:#ff1a2a;
    --wood-dark:#1c100b;
    --wood-mid:#3a2117;
    --ink:#2a0507;
    --white:#ffffff;
    --page:#ffffff;
  }
  *{box-sizing:border-box;margin:0;padding:0}
  html,body{width:1113px;height:1200px;overflow:hidden;background:var(--page)}
  .canvas{position:relative;width:1113px;height:1200px}

  .panel{position:absolute;overflow:hidden}
  .panel svg.shapes{position:absolute;inset:0;width:100%;height:100%}
  .photo{position:absolute;inset:0}

  .friday-post{left:86px;top:84px;width:485px;height:484px}
  .friday-post .photo{background:
      radial-gradient(ellipse at 35% 80%, #4a3a30 0%, transparent 45%),
      linear-gradient(90deg,#1a1613 0%,#2c2521 22%,#4a2a22 40%,#5a3024 70%,#3b241c 100%)}

  .event-post{left:83px;top:616px;width:488px;height:487px}
  .event-post .photo{background:
      radial-gradient(ellipse at 72% 40%, #a3282a 0%, transparent 40%),
      radial-gradient(ellipse at 25% 45%, #6b3a22 0%, transparent 50%),
      linear-gradient(180deg,#2a130d 0%,#4a2416 50%,#3a110c 100%)}

  .menu-card{left:625px;top:188px;width:406px;height:761px;background:
      repeating-linear-gradient(90deg,rgba(255,255,255,.025) 0 3px,transparent 3px 11px),
      linear-gradient(90deg,var(--wood-dark),var(--wood-mid) 50%,var(--wood-dark))}

  .brand{position:absolute;transform:translate(-50%,-50%);display:flex;align-items:center;gap:10px;white-space:nowrap}
  .brand-dot{width:14px;height:14px;border-radius:50%;background:var(--pub-red)}
  .brand-name{font-family:'Oswald',sans-serif;font-weight:500;color:var(--white);font-size:34px;letter-spacing:2px;line-height:1}
  .brand--small .brand-name{font-size:28px}
  .brand--small .brand-dot{width:12px;height:12px}

  .neon{position:absolute;transform:translate(-50%,-50%) rotate(-12deg);font-family:'Share Tech Mono',monospace;
      color:var(--neon);text-align:center;line-height:.95;white-space:nowrap;
      text-shadow:0 0 4px var(--neon-glow),0 0 10px var(--neon-glow),0 0 22px var(--neon-glow)}
  .neon--headline{font-size:80px}
  .neon--event{font-size:62px;transform:translate(-50%,-50%) rotate(-7deg)}
  .neon--menu{font-size:46px;transform:translate(-50%,-50%);font-style:italic;letter-spacing:3px}

  .event-detail{position:absolute;transform:translate(-50%,-50%) rotate(-32deg);font-family:'Oswald',sans-serif;
      font-size:24px;color:var(--ink);white-space:nowrap;letter-spacing:-.5px}

  .menu-list{position:absolute;left:56px;top:150px;width:300px;list-style:none}
  .menu-item{display:flex;align-items:baseline;height:34.5px;font-family:'Antonio',sans-serif;
      font-size:19px;color:var(--white);letter-spacing:3px}
  .menu-item .leader{flex:1;margin:0 6px;border-bottom:2px dotted rgba(255,255,255,.8);transform:translateY(-4px)}
</style>
</head>
<body>
<div class="canvas">

  <section class="panel friday-post">
    <div class="photo" role="img" aria-label="Photo of old wooden barrels against a brick pub wall"></div>
    <svg class="shapes" viewBox="0 0 637 637" preserveAspectRatio="none" aria-hidden="true">
      <polygon points="196,580 480,425 637,410 637,637 205,637" fill="var(--pub-red)" opacity=".55"/>
      <polygon points="339,562 637,409 637,637 376,637" fill="var(--pub-red)"/>
    </svg>
    <div class="brand" style="left:247px;top:96px">
      <span class="brand-dot"></span>
      <span class="brand-name">BRANNIGAN'S</span>
    </div>
    <div class="neon neon--headline" style="left:243px;top:266px">FRIDAY<br>SPECIAL</div>
  </section>

  <section class="panel event-post">
    <div class="photo" role="img" aria-label="Photo of a woman in a red dress in a warmly lit pub"></div>
    <svg class="shapes" viewBox="0 0 641 640" preserveAspectRatio="none" aria-hidden="true">
      <polygon points="0,500 420,395 115,555 0,590" fill="var(--pub-red)" opacity=".6"/>
      <polygon points="115,555 625,285 641,300 641,640 160,640" fill="var(--pub-red)"/>
    </svg>
    <div class="brand brand--small" style="left:135px;top:88px">
      <span class="brand-dot"></span>
      <span class="brand-name">BRANNIGAN'S</span>
    </div>
    <div class="neon neon--event" style="left:138px;top:248px">EVENT<br>NAME</div>
    <span class="event-detail" style="left:223px;top:401px">MORE DETAILS</span>
    <span class="event-detail" style="left:353px;top:341px">DATE</span>
    <span class="event-detail" style="left:437px;top:303px">TIME</span>
    <span class="event-detail" style="left:354px;top:385px">SPECIAL GUEST ARTIST NAME</span>
    <span class="event-detail" style="left:385px;top:405px">WWW.WEBSITE.COM</span>
  </section>

  <section class="panel menu-card">
    <svg class="shapes" viewBox="0 0 534 1000" preserveAspectRatio="none" aria-hidden="true">
      <polygon points="0,690 57,795 0,825" fill="var(--pub-red)"/>
      <polygon points="410,1000 534,935 534,1000" fill="var(--pub-red)"/>
    </svg>
    <div class="neon neon--menu" style="left:203px;top:61px">MENU</div>
    <ul class="menu-list">
      <li class="menu-item"><span>MENU ITEM 1</span><span class="leader"></span><span>$5</span></li>
      <li class="menu-item"><span>MENU ITEM 1</span><span class="leader"></span><span>$5</span></li>
      <li class="menu-item"><span>MENU ITEM 1</span><span class="leader"></span><span>$5</span></li>
      <li class="menu-item"><span>MENU ITEM 1</span><span class="leader"></span><span>$5</span></li>
      <li class="menu-item"><span>MENU ITEM 1</span><span class="leader"></span><span>$5</span></li>
      <li class="menu-item"><span>MENU ITEM 1</span><span class="leader"></span><span>$5</span></li>
      <li class="menu-item"><span>MENU ITEM 1</span><span class="leader"></span><span>$5</span></li>
      <li class="menu-item"><span>MENU ITEM 1</span><span class="leader"></span><span>$5</span></li>
      <li class="menu-item"><span>MENU ITEM 1</span><span class="leader"></span><span>$5</span></li>
      <li class="menu-item"><span>MENU ITEM 1</span><span class="leader"></span><span>$5</span></li>
    </ul>
    <div class="brand" style="left:206px;top:648px">
      <span class="brand-dot"></span>
      <span class="brand-name">BRANNIGAN'S</span>
    </div>
  </section>

</div>
</body>
</html>
```